VORN - Business cards

Business card to be created for Commercial sales staff

Target Market(s)

Commercial businesses

Industry/Entity Type

Commercial

Contact Information for Business Card

Look professional. For commercial clients

Colors
ffffff

Requirements
Must have
• - Vorn Logo
• - Commercial sales staff as postion
• - room for commerical sales manager role
• - person name and their mobile number
• - Website : vornelectrical.com.au
Nice to have
• White background.
• On back of business card just have the logo no other information
Should not have
• Should only have white background on front of card.

```html
<!DOCTYPE html>
<html lang="en">
<head>
<meta charset="utf-8">
<title>VORN – Business Cards</title>
<link rel="stylesheet" href="https://fonts.googleapis.com/css2?family=Questrial&display=swap">
<style>
  :root {
    --backdrop: #45403d;
    --card: #1c1c1e;
    --card-edge: #232325;
    --logo-grey: #34353a;
    --brand-red: #d7222b;
    --text-white: #f2f2f2;
  }
  * { margin: 0; padding: 0; box-sizing: border-box; }
  html, body {
    width: 1200px;
    height: 716px;
    overflow: hidden;
  }
  body {
    background: var(--backdrop);
    font-family: "Questrial", "Century Gothic", sans-serif;
    position: relative;
  }
  .card {
    position: absolute;
    top: 208px;
    width: 520px;
    height: 298px;
    background: var(--card);
    border: 1px solid var(--card-edge);
    border-radius: 4px;
  }
  .card--back { left: 50px; }
  .card--front { left: 630px; }

  .brand {
    position: absolute;
    display: flex;
    align-items: center;
    gap: 12px;
    left: 50%;
    transform: translateX(-50%);
  }
  .card--back .brand { top: 110px; }
  .card--front .brand { top: 62px; }
  .brand__dot {
    width: 22px;
    height: 22px;
    border-radius: 50%;
    background: var(--brand-red);
  }
  .brand__name {
    font-size: 62px;
    letter-spacing: 4px;
    color: var(--logo-grey);
    line-height: 1;
  }

  .person {
    position: absolute;
    left: 92px;
    top: 196px;
    text-align: right;
    width: 150px;
  }
  .person__name {
    color: var(--brand-red);
    font-size: 21px;
    line-height: 1.1;
  }
  .person__role {
    color: var(--text-white);
    font-size: 12px;
    text-align: left;
    margin-top: 2px;
  }
  .divider {
    position: absolute;
    left: 260px;
    top: 188px;
    width: 1px;
    height: 58px;
    background: var(--text-white);
  }
  .contact {
    position: absolute;
    left: 276px;
    top: 196px;
    list-style: none;
  }
  .contact__item {
    display: flex;
    align-items: center;
    gap: 9px;
    color: var(--text-white);
    font-size: 15px;
    letter-spacing: 0.5px;
    margin-bottom: 9px;
  }
  .contact__icon {
    width: 13px;
    height: 13px;
    flex: none;
  }
</style>
</head>
<body>
  <section class="card card--back" aria-label="Card back">
    <div class="brand">
      <span class="brand__dot"></span>
      <span class="brand__name">VORN</span>
    </div>
  </section>

  <section class="card card--front" aria-label="Card front">
    <div class="brand">
      <span class="brand__dot"></span>
      <span class="brand__name">VORN</span>
    </div>

    <div class="person">
      <p class="person__name">Daniel Reyes</p>
      <p class="person__role">manager</p>
    </div>

    <div class="divider"></div>

    <ul class="contact">
      <li class="contact__item">
        <svg class="contact__icon" viewBox="0 0 13 13" aria-hidden="true">
          <rect width="13" height="13" rx="2" fill="#d7222b"/>
          <path d="M4 3h1.6l.7 2-1 .8a5 5 0 0 0 2 2l.8-1 2 .7V9.1A1 1 0 0 1 9 10 6 6 0 0 1 3 4a1 1 0 0 1 1-1z" fill="#1c1c1e"/>
        </svg>
        <span>214-555-0182</span>
      </li>
      <li class="contact__item">
        <svg class="contact__icon" viewBox="0 0 13 13" aria-hidden="true">
          <rect width="13" height="13" rx="2" fill="#d7222b"/>
          <circle cx="6.5" cy="6.5" r="3.6" fill="none" stroke="#1c1c1e" stroke-width="1"/>
          <path d="M2.9 6.5h7.2M6.5 2.9c-1.6 2-1.6 5.2 0 7.2M6.5 2.9c1.6 2 1.6 5.2 0 7.2" fill="none" stroke="#1c1c1e" stroke-width="0.8"/>
        </svg>
        <span>vornelectrical.com.au</span>
      </li>
    </ul>
  </section>
</body>
</html>
```